Webseite Toilettenvermietung
Zielgruppe
Wir vermieten mobile Toilettenkabine und Toilettenwagen. Wir haben noch eine Webseite kabinenpark-nord.de und lokus-verleihhaus.de und benötigen noch eine weitere. Es sollen nur die Miettoiletten und Toilettenwagen beworben werden
Aufgabenstellung
saubere und aussageräftige, farbliches Erscheinungsbild der Startseite.

```html
<!DOCTYPE html>
<html lang="de">
<head>
<meta charset="utf-8">
<title>KLARWERK – WC Mietservice</title>
<link href="https://fonts.googleapis.com/css2?family=Roboto:wght@300;400;500&display=swap" rel="stylesheet">
<style>
:root{
  --blue:#2b6cb8;
  --blue-band-top:#2c7fd0;
  --blue-band-bottom:#1a5eae;
  --green:#8dbb12;
  --text:#555;
  --muted:#8a8a8a;
  --light-bg:#f2f2f2;
  --header-bg:#ececf0;
  --line:#dcdcdc;
}
*{box-sizing:border-box;margin:0;padding:0}
html,body{width:1062px;height:1200px;overflow:hidden;background:#fff}
body{font-family:'Roboto',sans-serif;font-weight:300;color:var(--text);position:relative}
.abs{position:absolute}
.btn{position:absolute;background:var(--green);color:#fff;font-weight:400;text-align:center;text-transform:uppercase;border-radius:1px}

/* header */
.site-header{position:absolute;left:0;top:0;width:1062px;height:39px;background:var(--header-bg);z-index:2}
.brand{position:absolute;left:200px;top:11px;display:flex;align-items:center;gap:5px;font-weight:500;font-size:14px;color:var(--blue);letter-spacing:.5px}
.brand-dot{width:10px;height:10px;border-radius:50%;background:var(--blue)}
.main-nav a{position:absolute;top:14px;font-size:9px;color:#444;text-decoration:none;font-weight:300}
.main-nav a.active{color:var(--blue)}

/* hero */
.hero{position:absolute;left:0;top:39px;width:1062px;height:314px;background:
 radial-gradient(ellipse at 78% 35%,rgba(200,60,220,.55),transparent 45%),
 radial-gradient(ellipse at 25% 40%,rgba(90,70,220,.6),transparent 50%),
 linear-gradient(180deg,#2a2466 0%,#1d1747 55%,#0c0a1c 100%)}
.hero-box{position:absolute;left:285px;top:96px;width:261px;height:118px;background:rgba(20,18,40,.72);border-radius:3px}
.hero-title{position:absolute;left:14px;top:11px;font-size:27px;font-weight:300;color:#2f7fd6;letter-spacing:-.3px}
.hero-text{position:absolute;left:15px;top:45px;width:215px;font-size:7.3px;line-height:10px;color:#ccc}
.hero-box .btn{left:15px;top:84px;width:111px;height:22px;font-size:9.5px;line-height:22px;font-weight:300}

/* welcome */
.welcome{position:absolute;left:0;top:353px;width:1062px;height:75px;border-bottom:1px solid var(--line);text-align:center}
.welcome h1{margin-top:18px;font-size:16.5px;line-height:20px;font-weight:300;color:var(--blue);text-transform:uppercase}

/* products */
.products{position:absolute;left:0;top:428px;width:1062px;height:326px;background:var(--light-bg)}
.section-title{position:absolute;left:0;width:1062px;text-align:center;font-size:16.5px;color:#444;font-weight:400}
.title-rule{position:absolute;left:499px;top:46px;width:64px;height:2px;background:#cfcfcf;border-radius:50%}
.product{position:absolute;top:65px;width:150px;text-align:center}
.product-img{margin:0 auto;border-radius:2px}
.product h3{position:absolute;top:119px;left:0;width:150px;font-size:10.5px;line-height:13.5px;font-weight:300;color:var(--blue)}
.product p{position:absolute;top:154px;left:0;width:150px;font-size:7px;line-height:9.3px;color:var(--muted)}
.product .btn{top:206px;left:25px;width:100px;height:21px;line-height:21px;font-size:9.5px;font-weight:300}
.col-rule{position:absolute;top:88px;width:1px;height:182px;background:var(--line)}

/* services band */
.services{position:absolute;left:0;top:754px;width:1062px;height:183px;background:linear-gradient(180deg,var(--blue-band-top),var(--blue-band-bottom));color:#fff}
.services h2{position:absolute;left:199px;top:18px;font-size:16.5px;line-height:20px;font-weight:300}
.services .intro{position:absolute;left:199px;top:73px;width:170px;font-size:7.4px;line-height:13.3px;font-weight:300}
.service{position:absolute;top:22px;width:130px;text-align:center}
.service .ring{width:52px;height:52px;margin:0 auto;border:1.5px solid #fff;border-radius:50%;display:flex;align-items:center;justify-content:center}
.service h3{margin-top:14px;font-size:12px;font-weight:500}
.service p{margin-top:5px;font-size:7.3px;line-height:13px;color:#dfeaf7}
.service .more{display:inline-block;margin-top:4px;font-size:7.6px;font-weight:500;color:#fff}

/* about + news */
.about{position:absolute;left:199px;top:959px;width:365px}
.about h2,.news h2{font-size:16.5px;font-weight:300;color:#444}
.about h2 span{color:var(--blue)}
.about p{margin-top:9px;font-size:7.3px;line-height:12.2px;color:var(--muted)}
.split-rule{position:absolute;left:596px;top:960px;width:1px;height:150px;background:var(--line)}
.news{position:absolute;left:624px;top:959px;width:240px}
.news .date{margin-top:11px;font-size:7.3px;color:#444}
.news h4{margin-top:4px;font-size:7.5px;font-weight:400;color:#444}
.news p{margin-top:6px;font-size:7.1px;line-height:12.2px;color:var(--muted)}
.news .more{margin-top:4px;font-size:7.5px;color:#444}

/* buy bar */
.buy-bar{position:absolute;left:0;top:1132px;width:1062px;height:46px;background:#f3f3f3;border-top:1px solid var(--line);border-bottom:1px solid var(--line)}
.buy-bar h3{position:absolute;left:356px;top:14px;font-size:13px;font-weight:400;color:#444}
.buy-bar .sub{position:absolute;left:538px;top:17px;font-size:10px;color:var(--muted)}
.buy-bar .btn{left:763px;top:13px;width:99px;height:19px;line-height:19px;font-size:9.5px;font-weight:300}
.buy-img{position:absolute;left:213px;top:1092px;width:74px;height:82px;background:linear-gradient(160deg,#3fb3d6,#1d7fa6);border-radius:3px;z-index:3}

/* footer */
.site-footer{position:absolute;left:0;top:1178px;width:1062px;height:22px}
.site-footer a{position:absolute;top:6px;font-size:7.6px;color:#777;text-decoration:none}
</style>
</head>
<body>

<header class="site-header">
  <div class="brand"><span class="brand-dot"></span>KLARWERK</div>
  <nav class="main-nav">
    <a class="active" style="left:557px">Startseite</a>
    <a style="left:638px">Miettoiletten</a>
    <a style="left:730px">Toilettenwagen</a>
    <a style="left:832px">Kontakt</a>
  </nav>
</header>

<section class="hero" role="img" aria-label="Konzertfoto: jubelndes Publikum vor einer beleuchteten Bühne mit Band">
  <div class="hero-box">
    <div class="hero-title">KOMMSTE MIT?</div>
    <p class="hero-text">Lorem Ipsum is simply dummy text of the printing and type-setting industry. Lorem Ipsum has been the industry's standard dummy text ever since the 1500s....</p>
    <span class="btn">Contact us</span>
  </div>
</section>

<section class="welcome">
  <h1>Willkommen bei KLARWERK, Ihr WC Mietservice für mobile WC<br>Kabinen, Wagen &amp; Container</h1>
</section>

<section class="products">
  <h2 class="section-title" style="top:24px">Products</h2>
  <div class="title-rule"></div>

  <article class="product" style="left:193px">
    <div class="product-img" role="img" aria-label="Blaue mobile WC-Kabine" style="width:56px;height:96px;background:linear-gradient(90deg,#1a5db8,#2b8be0)"></div>
    <h3>Mobile Wc Kabinen<br>Mieten</h3>
    <p>Unsere WC-Kabinen zum mieten bzw im Verleih. Hier finden Sie unsere Toilettenk-abinen wie z. B. das mobile Baustellen WC, unser Universal Miete WC oder den Urinalstand in der Übersicht.</p>
    <span class="btn">Details</span>
  </article>
  <div class="col-rule" style="left:355px"></div>

  <article class="product" style="left:368px">
    <div class="product-img" role="img" aria-label="WC-Container mit mehreren Türen" style="width:90px;height:62px;margin-top:17px;background:linear-gradient(90deg,#8f95a0,#e4e6ec);border:2px solid #2c2d74"></div>
    <h3>Mobile Wc Container<br>Mieten</h3>
    <p>Sie sind auf der Suche nach einem mo-bilen WC Container, bzw. Toilettencontain-er zum mieten? Hier finden Sie unsere mobilen WC Container und WC-Anlagen im Verleih in der Übersicht.</p>
    <span class="btn">Details</span>
  </article>
  <div class="col-rule" style="left:530px"></div>

  <article class="product" style="left:543px">
    <div class="product-img" role="img" aria-label="Graue WC-Kabine" style="width:52px;height:84px;margin-top:6px;background:linear-gradient(90deg,#6b7078,#b9bcc2)"></div>
    <h3>Mobile Wc Wagen<br>Mieten</h3>
    <p>Hier finden Sie unsere WC Wagen in der Übersicht zur Vermietung, zum Verleih. Vom normalen Toilettenwagen (1x Dame / 1x Herren) bis hin zum exklusiven WC Wagen / Toilettenwagen.</p>
    <span class="btn">Details</span>
  </article>
  <div class="col-rule" style="left:705px"></div>

  <article class="product" style="left:718px">
    <div class="product-img" role="img" aria-label="Weißer Toilettenwagen mit zwei Türen" style="width:102px;height:50px;margin-top:22px;background:linear-gradient(180deg,#f7f8fb 75%,#3a3f9a 75%);border:1px solid #ccd"></div>
    <h3>Mobile Wc Anlagen<br>Kaufen</h3>
    <p>Unser Marktplatz. Hier finden Sie div. WC Kabinen, Sanitärcontainer, Toilettenwa-gen, Urinalstände sowie mobile WC Wagen zum verkauf. Neue und geb-rauchte WC Kabinen in verschiedenen</p>
    <span class="btn">Details</span>
  </article>
</section>

<section class="services">
  <h2>KLARWERK<br>Toilettenvermietung</h2>
  <p class="intro">Lorem Ipsum is simply dummy text of the print-ing and typesetting industry.<br>Lorem Ipsum has been the industry's standard dummy text ever since the 1500s when an unknown printer took a galley of type and scrambled it to make a type specimen book.</p>

  <div class="service" style="left:420px">
    <div class="ring">
      <svg width="26" height="26" viewBox="0 0 26 26" fill="none" stroke="#fff" stroke-width="1.6" stroke-linecap="round"><path d="M21 4l-7 9"/><path d="M14 13c-3-1-6 0-8 3l6 5c2-2 3-5 2-8z"/><path d="M8 18l-2 3M10 19l-1 3"/><circle cx="17" cy="22" r="1" fill="#fff"/><circle cx="20" cy="19" r=".8" fill="#fff"/></svg>
    </div>
    <h3>Clean</h3>
    <p>Lorem Ipsum is simply<br>dummy text of the printing and<br>typesetting industry.</p>
    <span class="more">Read More ›</span>
  </div>

  <div class="service" style="left:582px">
    <div class="ring">
      <svg width="30" height="22" viewBox="0 0 30 22" fill="#fff"><rect x="1" y="3" width="17" height="12" rx="1"/><path d="M19 7h5l4 5v5h-9z"/><circle cx="7" cy="17" r="3" stroke="#1f6cc0" stroke-width="1.5"/><circle cx="23" cy="17" r="3" stroke="#1f6cc0" stroke-width="1.5"/></svg>
    </div>
    <h3>Transport</h3>
    <p>Lorem Ipsum is simply<br>dummy text of the printing and<br>typesetting industry.</p>
    <span class="more">Read More ›</span>
  </div>

  <div class="service" style="left:744px">
    <div class="ring">
      <svg width="26" height="26" viewBox="0 0 26 26" fill="none" stroke="#fff" stroke-width="2.6" stroke-linecap="round"><path d="M5 5l16 16"/><path d="M20 4l-3 3 2 2 3-3M17 7L6 20"/><path d="M3 6l3-3"/></svg>
    </div>
    <h3>Installation</h3>
    <p>Lorem Ipsum is simply<br>dummy text of the printing and<br>typesetting industry.</p>
    <span class="more">Read More ›</span>
  </div>
</section>

<section class="about">
  <h2>About <span>KLARWERK</span></h2>
  <p>Lorem Ipsum is simply dummy text of the printing and typesetting industry.<br>Lorem Ipsum has been the industry's standard dummy text ever since the 1500s, when an unknown printer took a galley of type and scrambled it to make a type specimen book.<br>It has survived not only five centuries, but also the leap into electronic typesetting, remaining essentially unchanged.<br>It was popularised in the 1960s with the release of Typoset sheets containing Lorem Ipsum passages, and more recently with desktop publishing software like Satzwerk Studio including versions of Lorem Ipsum.<br>Lorem Ipsum is simply dummy text of the printing and typesetting industry.</p>
</section>
<div class="split-rule"></div>
<section class="news">
  <h2>News &amp; Infos</h2>
  <div class="date">04.02.2014</div>
  <h4>Vermietung von mobilen, behindertengerechter WC Kabinen</h4>
  <p>Bei uns erhalten Sie nicht nur herkömmliche Mobil-WCs zur Miete. Ein bundesweiter Service unsers Unternehmens ist die Vermietung behin-dertengerechter WC Kabinen mit den Maßen 1,6 x 1,6 Metern und einer Außenhöhe von 2,30 Metern. Nutzen Sie die komfortable Alter-native der mobilen WC Anlagen für Ihre Veranstaltungen und/oder Baustellen.</p>
  <div class="more">Weitere Meldungen ›</div>
</section>

<div class="buy-img" role="img" aria-label="Türkisfarbene mobile Toilettenkabine"></div>
<section class="buy-bar">
  <h3>Mobile Toiletten Zum Kaufen</h3>
  <span class="sub">Jetzt In Unserem Marktplaz Stobern</span>
  <span class="btn">Buy it now</span>
</section>

<footer class="site-footer">
  <a style="left:199px">Produkte</a>
  <a style="left:238px">News &amp; Infos</a>
  <a style="left:292px">Unternehmen</a>
  <a style="left:347px">Kontakt</a>
  <a style="left:382px">AGB</a>
  <a style="left:404px">Impressum</a>
</footer>

</body>
</html>
```